Wordpress Design for my Consulting Company

We want a WordPress site created for our new business. We have created a mock-up of the content we want on the site at https://marcusdellow.example-sites.com/website-5

We are not attached to any of the pictures and just put stock stuff from wix's editor, which we don't have rights to use outside of wix.

We are NOT looking to just port this site to WordPress, we are looking for some creative ways to display the content in a more professional artistic sense.

I have included several logo files and a text file with the colors and Fonts used in the logo. We are not looking to change the logo or the colors used in the logo.

The Schedule appointment links to a page that embeds a bookingnest.example.com calendar. https://bookingnest.example.com/marcus-dellow/brightvale

The final website domain will be enterprisebrightvale.example

Enterprise brightvale is a consulting company that works directly with the business owners and leaders of small businesses between 50-200 employees. We help companies make sure they have the right technology to meet their strategic goals. We are the anti-"Computer Guy" and we focus on business outcomes NOT cool technology gadgets.

The final design should communicate business growth and success.

Target Market(s)

Business Owners of companies with 50-200 employees

Coding

Coded - Design and coding required

Number of Pages Required

1 page

Font styles to use
Serif
Other font styles liked:
• Trajan Pro Bold, Open Sans

Requirements
Must have
• Should focus on consulting rather than technology.
• Should show the customer as the hero and we are just their guide.
• Must use the logo provided and the colors and fonts in the text file provided. Any other colors and fonts must be complementary.
• The design should scale for all devices computer, iPad, or phone
Should not have
• Should not focus on technology, we are the anti-"Computer Guy" and we focus on business outcomes NOT cool technology gadgets.

```html
<!DOCTYPE html>
<html lang="en">
<head>
<meta charset="utf-8">
<title>Brightvale — Technology Advisors That Get Business</title>
<link rel="stylesheet" href="https://fonts.googleapis.com/css2?family=Cinzel:wght@400;700&family=Open+Sans:ital,wght@0,400;0,600;0,700;1,400&family=Caveat:wght@400;600&family=Kalam:wght@400&display=swap">
<style>
:root{
  --orange:#c8773f;
  --orange-soft:#d08a5a;
  --slate:#3e4a53;
  --slate-deep:#333e46;
  --ink:#2d3338;
  --text:#5d6368;
  --muted:#8a9096;
  --line:#e3e5e7;
  --paper:#ffffff;
  --mist:#f1f2f3;
  --sand:#f7f2ec;
  --footer:#eeeff0;
}
*{box-sizing:border-box;margin:0;padding:0}
html,body{width:1200px;height:2575px;overflow:hidden}
body{background:var(--paper);font-family:"Open Sans",Arial,sans-serif;color:var(--text)}
.page{position:relative;width:1200px;height:2575px;overflow:hidden}
.abs{position:absolute}

/* header */
.site-header{left:0;top:0;width:1200px;height:88px;background:var(--paper)}
.brand{display:flex;align-items:center;gap:10px;color:var(--slate);font-family:"Cinzel",Georgia,serif;font-weight:700;font-size:19px;letter-spacing:.5px}
.brand-dot{width:40px;height:40px;border-radius:50%;background:var(--slate)}
.site-header .brand{position:absolute;left:257px;top:24px}
.nav{position:absolute;top:46px;left:0;width:1200px;font-size:9.5px;letter-spacing:.6px;color:var(--ink);text-transform:uppercase}
.nav a{position:absolute;color:inherit;text-decoration:none}

/* hero */
.hero{left:0;top:88px;width:1200px;height:472px;overflow:hidden}
.hero-scene{position:absolute;inset:0;background:linear-gradient(90deg,#8d8579 0%,#b3a998 30%,#a79c8c 55%,#c8c2b8 100%)}
.hero-portrait{position:absolute;left:690px;top:0;width:510px;height:472px;background:radial-gradient(ellipse at 55% 30%,#d9c4ae 0%,#c9b9a6 30%,rgba(226,223,218,.9) 60%,rgba(180,172,160,0) 85%)}
.hero-shade{position:absolute;inset:0;background:linear-gradient(90deg,rgba(60,62,64,.25),rgba(60,62,64,.35) 50%,rgba(60,62,64,0) 85%)}
.hero-copy{position:absolute;left:300px;top:110px;width:580px;text-align:center;color:#fff}
.eyebrow{font-size:10px;letter-spacing:3px;text-transform:uppercase;color:#3a3f44;font-weight:600}
.eyebrow em{font-style:normal;color:var(--orange)}
.eyebrow-rule{width:26px;height:2px;background:var(--orange);margin:12px auto 14px}
.hero h1{font-family:"Cinzel",Georgia,serif;font-weight:700;font-size:35px;line-height:39px;letter-spacing:.5px;text-shadow:0 1px 6px rgba(0,0,0,.25)}
.btn{display:inline-flex;align-items:center;gap:10px;height:34px;padding:0 18px;font-size:10px;letter-spacing:.8px;text-transform:uppercase;color:#fff;text-decoration:none;font-weight:600}
.btn-orange{background:var(--orange)}
.btn-slate{background:var(--slate)}
.btn svg{width:11px;height:8px}
.hero-actions{margin-top:26px;display:flex;justify-content:center;gap:6px}
.hero-notch{position:absolute;left:520px;bottom:-1px;width:160px;height:14px}

/* section titles */
.section-title{font-family:"Cinzel",Georgia,serif;font-weight:700;font-size:20px;letter-spacing:.5px;color:var(--ink);text-align:center;width:1200px;left:0}
.section-title em{font-style:normal;color:var(--orange)}
.title-rule{width:26px;height:2px;background:var(--orange);left:587px}
.section-sub{width:1200px;left:0;text-align:center;font-size:12.5px;color:var(--ink)}

/* why */
.gripe-list{width:200px;list-style:none}
.gripe-list li{display:flex;gap:8px;align-items:flex-start;padding:10px 0;border-bottom:1px solid var(--line);font-family:"Caveat",cursive;font-size:15.5px;line-height:17px;color:var(--orange)}
.gripe-list li:last-child{border-bottom:none}
.gripe-left li{flex-direction:row-reverse;text-align:right}
.tick{flex:0 0 11px;width:11px;height:11px;margin-top:2px}
.why-ring{left:465px;top:686px;width:270px;height:270px}
.why-photo{position:absolute;left:13px;top:13px;width:244px;height:244px;border-radius:50%;background:radial-gradient(circle at 50% 40%,#d4d5d6 0%,#a8aaac 55%,#6d7175 100%)}

/* what */
.what{left:0;top:988px;width:1200px;height:382px}
.what-band{position:absolute;inset:0;clip-path:polygon(0 14px,100% 4px,100% 364px,0 376px);background:linear-gradient(90deg,#c98252 0%,#8c6a55 18%,#4f5359 38%,var(--slate) 60%,var(--slate-deep) 100%)}
.what-edge-top{position:absolute;left:0;top:0;width:1200px;height:16px;background:#c4c8cc;clip-path:polygon(0 8px,100% 0,100% 4px,0 14px)}
.what-edge-bottom{position:absolute;left:0;top:360px;width:1200px;height:22px;background:#e8c6ad;clip-path:polygon(0 16px,100% 4px,100% 6px,0 20px)}
.what-photo{position:absolute;left:243px;top:80px;width:338px;height:212px;background:linear-gradient(180deg,#c9ccc8 0%,#9ea39a 45%,#5f7a45 70%,#a66c50 100%);box-shadow:0 6px 14px rgba(0,0,0,.3)}
.what-copy{position:absolute;left:606px;top:88px;width:330px;text-align:center;color:#e9ecee;font-size:10.5px;line-height:16px}
.what-copy h2{font-family:"Cinzel",Georgia,serif;font-weight:700;font-size:20px;color:#fff;letter-spacing:.5px}
.what-copy h2 em{font-style:normal;color:var(--orange)}
.what-copy .rule{width:26px;height:2px;background:var(--orange);margin:10px auto 18px}
.what-copy p{margin-bottom:12px}
.what-copy .btn{margin-top:10px}

/* how */
.steps{left:243px;top:1517px;width:712px;height:192px;display:flex}
.step{flex:1;text-align:center;padding:26px 16px 0}
.step:nth-child(odd){background:var(--mist)}
.step:nth-child(even){background:var(--sand)}
.step svg{width:36px;height:36px;stroke:var(--ink);fill:none;stroke-width:1.6}
.step h3{font-family:"Kalam",cursive;font-weight:400;font-size:12.5px;letter-spacing:1.2px;color:var(--ink);margin-top:18px}
.step .rule{width:18px;height:2px;background:var(--orange);margin:8px auto 10px}
.step p{font-size:9.5px;line-height:14px;color:var(--text)}

/* testimonials */
.testimonials{left:0;top:1786px;width:1200px;height:357px;overflow:hidden}
.testimonial-scene{position:absolute;inset:0;background:linear-gradient(90deg,#5d5c58 0%,#4d565c 25%,#46535b 60%,#4b565d 100%)}
.testimonial-shade{position:absolute;inset:0;background:rgba(52,64,73,.72)}
.testimonial-body{position:absolute;left:0;top:48px;width:1200px;text-align:center;color:#fff}
.testimonial-body h2{font-family:"Cinzel",Georgia,serif;font-weight:700;font-size:20px;letter-spacing:.5px}
.testimonial-body h2 em{font-style:normal;color:var(--orange)}
.quote-mark{display:block;margin:14px auto 0;width:34px;height:28px}
.testimonial-body blockquote{width:440px;margin:16px auto 0;font-style:italic;font-size:10.5px;line-height:17px;color:#eef0f1}
.avatar{width:36px;height:36px;border-radius:50%;margin:14px auto 0;background:linear-gradient(180deg,#c9a98e,#6d6660);border:2px solid #fff}
.client-name{margin-top:6px;font-size:10.5px;font-weight:700;color:var(--orange)}
.client-role{font-size:9.5px;color:#fff}
.dots{display:flex;gap:6px;justify-content:center;margin-top:18px}
.dots span{width:5px;height:5px;border-radius:50%;background:rgba(255,255,255,.4)}
.dots span:first-child{background:#fff}
.arrow{position:absolute;top:170px;width:12px;height:14px}

/* contact */
.contact{left:0;top:2143px;width:1200px;height:340px;background:var(--mist)}
.contact-title{position:absolute;left:300px;top:38px;width:240px;text-align:center;font-family:"Cinzel",Georgia,serif;font-weight:700;font-size:20px;color:var(--ink)}
.contact-title em{font-style:normal;color:var(--orange)}
.contact-item{position:absolute;left:269px;width:300px}
.contact-item h4{display:flex;align-items:center;gap:8px;font-family:"Cinzel",Georgia,serif;font-weight:700;font-size:12px;letter-spacing:1px;color:var(--ink)}
.contact-item h4 svg{width:14px;height:14px}
.contact-item p{margin-top:10px;font-size:9.5px;line-height:15px;color:var(--text)}
.message-panel{position:absolute;left:596px;top:0;width:352px;height:340px;background:var(--slate);padding:38px 31px 0}
.message-panel h3{font-family:"Cinzel",Georgia,serif;font-weight:700;font-size:11px;letter-spacing:1.6px;color:#fff}
.field{display:block;width:292px;height:29px;margin-top:10px;background:#fff;border:none;padding:0 10px;font-size:8.5px;letter-spacing:.8px;color:#9aa0a5;line-height:29px;text-transform:uppercase}
.field:first-of-type{margin-top:12px}
.field-area{height:78px;line-height:22px}
.submit{display:block;margin-top:14px;width:113px;height:27px;background:var(--orange);color:#fff;font-size:9px;letter-spacing:1px;font-weight:600;text-align:center;line-height:27px;text-transform:uppercase}
.contact-stripe{left:0;top:2458px;width:1200px;height:30px}

/* footer */
.site-footer{left:0;top:2487px;width:1200px;height:88px;background:var(--footer)}
.site-footer .brand{position:absolute;left:257px;top:24px}
.social{position:absolute;left:874px;top:13px;display:flex;gap:8px}
.social span{width:20px;height:20px;border-radius:50%;border:1px solid #9ca2a7;background:#fff}
.copyright{position:absolute;right:252px;top:45px;font-size:9px;color:var(--muted)}
</style>
</head>
<body>
<div class="page">

  <header class="site-header abs">
    <div class="brand"><span class="brand-dot"></span>Brightvale</div>
    <nav class="nav">
      <a href="#why" style="left:622px">Why Us</a>
      <a href="#what" style="left:675px">What We Do</a>
      <a href="#how" style="left:749px">How We Do It</a>
      <a href="#testimonials" style="left:828px">Testimonials</a>
      <a href="#contact" style="left:907px">Contact</a>
    </nav>
  </header>

  <section class="hero abs">
    <div class="hero-scene" role="img" aria-label="Softly blurred modern office interior with tall windows"></div>
    <div class="hero-portrait" role="img" aria-label="Smiling businessman in a white shirt and navy tie"></div>
    <div class="hero-shade"></div>
    <div class="hero-copy">
      <p class="eyebrow">Technology advisors that <em>get</em> business</p>
      <div class="eyebrow-rule"></div>
      <h1>We help you leverage<br>technology to create a<br>competitive advantage.</h1>
      <div class="hero-actions">
        <a class="btn btn-orange" href="https://bookingnest.example.com/marcus-dellow/brightvale">Schedule Appointment <svg viewBox="0 0 11 8"><path d="M0 4h9M6 1l3 3-3 3" stroke="#fff" fill="none" stroke-width="1.4"/></svg></a>
        <a class="btn btn-slate" href="#why">Keep Learning More <svg viewBox="0 0 11 8"><path d="M0 4h9M6 1l3 3-3 3" stroke="#fff" fill="none" stroke-width="1.4"/></svg></a>
      </div>
    </div>
    <svg class="hero-notch" viewBox="0 0 160 14" preserveAspectRatio="none"><path d="M0 14 C40 14 50 2 80 2 C110 2 120 14 160 14Z" fill="#fff"/></svg>
  </section>

  <section id="why">
    <h2 class="section-title abs" style="top:602px"><em>Why</em> Brightvale ?</h2>
    <p class="section-sub abs" style="top:645px">Are you tired of "Computer Guys" that...</p>

    <ul class="gripe-list gripe-left abs" style="left:249px;top:708px">
      <li><svg class="tick" viewBox="0 0 11 11"><circle cx="5.5" cy="5.5" r="5.5" fill="#2d3338"/><path d="M3 5.6l1.7 1.7L8 4" stroke="#fff" fill="none" stroke-width="1.4"/></svg><span>Don't want to be involved in business strategy.</span></li>
      <li><svg class="tick" viewBox="0 0 11 11"><circle cx="5.5" cy="5.5" r="5.5" fill="#2d3338"/><path d="M3 5.6l1.7 1.7L8 4" stroke="#fff" fill="none" stroke-width="1.4"/></svg><span>Say "No!" but do not give options on how to achieve your business outcome.</span></li>
      <li><svg class="tick" viewBox="0 0 11 11"><circle cx="5.5" cy="5.5" r="5.5" fill="#2d3338"/><path d="M3 5.6l1.7 1.7L8 4" stroke="#fff" fill="none" stroke-width="1.4"/></svg><span>Can't explain how a technology will create business value, but insist it is necessary.</span></li>
    </ul>

    <div class="why-ring abs">
      <svg viewBox="0 0 270 270" width="270" height="270" style="position:absolute;left:0;top:0">
        <path d="M135 3 A132 132 0 0 0 135 267" stroke="#c8773f" stroke-width="3" fill="none"/>
        <path d="M135 3 A132 132 0 0 1 135 267" stroke="#3e4a53" stroke-width="3" fill="none"/>
      </svg>
      <div class="why-photo" role="img" aria-label="Frustrated office worker resting his head on a laptop keyboard"></div>
    </div>

    <ul class="gripe-list abs" style="left:742px;top:708px">
      <li><svg class="tick" viewBox="0 0 11 11"><circle cx="5.5" cy="5.5" r="5.5" fill="#2d3338"/><path d="M3 5.6l1.7 1.7L8 4" stroke="#fff" fill="none" stroke-width="1.4"/></svg><span>Give you the excuse, "You never asked."</span></li>
      <li><svg class="tick" viewBox="0 0 11 11"><circle cx="5.5" cy="5.5" r="5.5" fill="#2d3338"/><path d="M3 5.6l1.7 1.7L8 4" stroke="#fff" fill="none" stroke-width="1.4"/></svg><span>Recommend technology when a simple process or policy change would have the same effect.</span></li>
      <li><svg class="tick" viewBox="0 0 11 11"><circle cx="5.5" cy="5.5" r="5.5" fill="#2d3338"/><path d="M3 5.6l1.7 1.7L8 4" stroke="#fff" fill="none" stroke-width="1.4"/></svg><span>Suggest expensive solutions that are just thrown away, soon after they are deployed.</span></li>
    </ul>
  </section>

  <section id="what" class="what abs">
    <div class="what-edge-top"></div>
    <div class="what-band"></div>
    <div class="what-edge-bottom"></div>
    <div class="what-photo" role="img" aria-label="Businessman with a briefcase walking toward a city skyline where a path splits in two"></div>
    <div class="what-copy">
      <h2><em>What</em> We Do</h2>
      <div class="rule"></div>
      <p>We get the frustration of working with consultants and experts who don't listen or take the time to understand your company goals and vision. We believe technology should serve your business, not the other way around.</p>
      <p>Computer guys frustrate business leaders because they don't have a business mindset. Brightvale advises on strategy that helps companies apply technology to gain a competitive advantage.</p>
      <a class="btn btn-orange" href="https://bookingnest.example.com/marcus-dellow/brightvale">Schedule Appointment <svg viewBox="0 0 11 8"><path d="M0 4h9M6 1l3 3-3 3" stroke="#fff" fill="none" stroke-width="1.4"/></svg></a>
    </div>
  </section>

  <section id="how">
    <h2 class="section-title abs" style="top:1418px"><em>How</em> We Do It</h2>
    <p class="section-sub abs" style="top:1462px">The Four Steps to <span style="color:var(--slate);font-weight:600">Aligning</span> Technology to your Business Strategy!</p>
    <div class="steps abs">
      <article class="step">
        <svg viewBox="0 0 36 36"><circle cx="18" cy="14" r="8"/><path d="M14 22v4h8v-4M15 30h6M18 2v3M6 14H3M33 14h-3M9 5l2 2M27 5l-2 2"/></svg>
        <h3>01.DISCOVER</h3><div class="rule"></div>
        <p>Identify what is going on behind the scenes, and create a snapshot of the current infrastructure.</p>
      </article>
      <article class="step">
        <svg viewBox="0 0 36 36"><rect x="4" y="4" width="13" height="13" stroke="#c8773f"/><rect x="19" y="4" width="13" height="13"/><rect x="4" y="19" width="13" height="13"/><rect x="19" y="19" width="13" height="13"/></svg>
        <h3>02.PRIORITIZE</h3><div class="rule"></div>
        <p>Meet to decide which solutions and policies will have the greatest impact on reaching the companies goals.</p>
      </article>
      <article class="step">
        <svg viewBox="0 0 36 36"><path d="M7 3h16l6 6v24H7z"/><circle cx="17" cy="19" r="7"/><path d="M17 12v7h7" stroke="#c8773f"/></svg>
        <h3>03.IMPLEMENT</h3><div class="rule"></div>
        <p>Implement those things that will give the greatest return on investment.</p>
      </article>
      <article class="step">
        <svg viewBox="0 0 36 36"><circle cx="13" cy="14" r="7"/><circle cx="13" cy="14" r="2.5"/><circle cx="25" cy="26" r="5"/><circle cx="25" cy="26" r="1.8"/><path d="M13 4v3M13 21v3M3 14h3M20 14h3M25 18v2M25 32v2M17 26h2M31 26h2"/></svg>
        <h3>04.MAINTAIN</h3><div class="rule"></div>
        <p>Create a system that keeps your technology aligned as strategy adjusts over time.</p>
      </article>
    </div>
  </section>

  <section id="testimonials" class="testimonials abs">
    <div class="testimonial-scene" role="img" aria-label="Woman working on a laptop at a desk by a bright window"></div>
    <div class="testimonial-shade"></div>
    <svg class="arrow" style="left:251px" viewBox="0 0 12 14"><path d="M8 2L3 7l5 5" stroke="#fff" stroke-width="2" fill="none"/></svg>
    <svg class="arrow" style="left:937px" viewBox="0 0 12 14"><path d="M4 2l5 5-5 5" stroke="#fff" stroke-width="2" fill="none"/></svg>
    <div class="testimonial-body">
      <h2><em>Client</em> Testimonials</h2>
      <svg class="quote-mark" viewBox="0 0 34 28"><path d="M2 28V16C2 8 6 3 14 1l1 4c-4 2-6 5-6 9h6v14zM19 28V16c0-8 4-13 12-15l1 4c-4 2-6 5-6 9h6v14z" fill="#c8773f"/></svg>
      <blockquote>I knew I was behind, I just didn't know by how much. We had years of band-aided solutions and Brightvale helped us stabilize our environment and position ourselves to compete in the quickly changing world of copy and print.</blockquote>
      <div class="avatar" role="img" aria-label="Portrait of the client"></div>
      <p class="client-name">Dean Whitacre</p>
      <p class="client-role">Founder, Print Harbor</p>
      <div class="dots"><span></span><span></span></div>
    </div>
  </section>

  <section id="contact" class="contact abs">
    <h2 class="contact-title"><em>Contact</em> Us</h2>
    <div class="contact-item" style="top:76px">
      <h4><svg viewBox="0 0 14 14"><circle cx="7" cy="7" r="7" fill="#c8773f"/><path d="M7 3a2.6 2.6 0 0 0-2.6 2.6C4.4 8 7 11 7 11s2.6-3 2.6-5.4A2.6 2.6 0 0 0 7 3z" fill="#fff"/><circle cx="7" cy="5.6" r="1" fill="#c8773f"/></svg>Our Address</h4>
      <p>418 Linden Crossing Drive, Suite 210,<br>Fairhollow, TX 75501</p>
    </div>
    <div class="contact-item" style="top:144px">
      <h4><svg viewBox="0 0 14 14"><circle cx="7" cy="7" r="7" fill="#c8773f"/><path d="M4.6 3.6l1.4-.3.8 1.9-.9.7c.4.9 1.2 1.7 2.1 2.1l.7-.9 1.9.8-.3 1.4c-3.2.3-6-2.5-5.7-5.7z" fill="#fff"/></svg>Call Us</h4>
      <p>(555) 014-2876</p>
    </div>
    <div class="contact-item" style="top:196px">
      <h4><svg viewBox="0 0 14 14"><circle cx="7" cy="7" r="7" fill="#c8773f"/><rect x="3.5" y="4.5" width="7" height="5" fill="#fff"/><path d="M3.5 4.5L7 7.3l3.5-2.8" stroke="#c8773f" fill="none" stroke-width=".8"/></svg>E-Mail</h4>
      <p>mdellow@enterprisebrightvale.example</p>
    </div>
    <form class="message-panel">
      <h3>Send Us a Message</h3>
      <span class="field">Name</span>
      <span class="field">Email</span>
      <span class="field field-area">Message</span>
      <span class="submit">Submit</span>
    </form>
  </section>

  <svg class="contact-stripe abs" viewBox="0 0 1200 30" preserveAspectRatio="none"><path d="M0 24 L1200 8 L1200 30 L0 30Z" fill="#c8773f"/></svg>

  <footer class="site-footer abs">
    <div class="brand"><span class="brand-dot"></span>Brightvale</div>
    <div class="social" aria-label="Social links"><span aria-label="Social profile one"></span><span aria-label="Social profile two"></span><span aria-label="Social profile three"></span></div>
    <p class="copyright">Copyright © 2018 Enterprise Brightvale. All Rights Reserved.</p>
  </footer>

</div>
</body>
</html>
```